immediate money for financial solutions

We need a Clean yet, eye catching, Business Card denoting a professional financial/tech firm. The front should have our logo and the notion that we are money lenders that get business loans quickly & easily. Maybe shade the colors of our logo. We are opened, but not committed to an unusual shaped card. The Back Should have our Business Contact Info & logo found on our website's front page: KORVANTINC.COM

Financial

```html
<!DOCTYPE html>
<html lang="en">
<head>
<meta charset="utf-8">
<title>Korvant Inc — Business Card</title>
<link rel="stylesheet" href="https://fonts.googleapis.com/css2?family=Open+Sans:wght@400;600&family=Oswald:wght@700&display=swap">
<style>
  :root {
    --paper: #ffffff;
    --wave-1: #eaf8ef;
    --wave-2: #cdf1da;
    --wave-3: #a8e9bf;
    --wave-4: #7fdea0;
    --wave-5: #5ad48b;
    --wave-teal: #72dcc4;
    --brand-green: #2f9a4a;
    --name-green: #3aa845;
    --title-green: #4b9a3f;
    --contact-ink: #1d5b48;
    --footer-ink: #274636;
  }
  html, body {
    margin: 0;
    padding: 0;
    overflow: hidden;
    background: var(--paper);
  }
  .card {
    position: relative;
    width: 1200px;
    height: 675px;
    overflow: hidden;
    background: var(--paper);
    font-family: "Open Sans", Arial, sans-serif;
  }
  .card__waves {
    position: absolute;
    inset: 0;
  }
  .brand {
    position: absolute;
    left: 645px;
    top: 100px;
    width: 470px;
    display: flex;
    flex-direction: column;
    align-items: center;
  }
  .brand__mark {
    width: 22px;
    height: 22px;
    background: var(--brand-green);
    margin-bottom: 16px;
  }
  .brand__name {
    margin: 0;
    font-size: 60px;
    font-weight: 600;
    letter-spacing: 1px;
    color: var(--brand-green);
    line-height: 1;
  }
  .brand__rule {
    width: 470px;
    height: 3px;
    background: var(--brand-green);
    margin-top: 14px;
  }
  .brand__tagline {
    margin: 10px 0 0;
    font-size: 34px;
    font-weight: 400;
    letter-spacing: 2px;
    color: var(--brand-green);
    line-height: 1;
  }
  .person {
    position: absolute;
    left: 714px;
    top: 282px;
  }
  .person__name {
    margin: 0;
    font-family: "Oswald", "Arial Narrow", sans-serif;
    font-weight: 700;
    font-size: 56px;
    letter-spacing: 2px;
    line-height: 1;
    color: var(--name-green);
    text-shadow: 1px 2px 2px rgba(0,0,0,0.25);
  }
  .person__title {
    margin: 6px 0 0;
    font-size: 31px;
    font-weight: 600;
    letter-spacing: 1px;
    color: var(--title-green);
    line-height: 1.1;
  }
  .contact {
    position: absolute;
    left: 78px;
    top: 444px;
    margin: 0;
    display: grid;
    grid-template-columns: 180px auto;
    row-gap: 2px;
    font-size: 28px;
    line-height: 38px;
    color: var(--contact-ink);
  }
  .contact dt, .contact dd { margin: 0; }
  .contact dd { font-weight: 600; letter-spacing: 0.5px; }
  .footer-note {
    position: absolute;
    left: 76px;
    top: 608px;
    margin: 0;
    font-size: 19px;
    line-height: 26px;
    color: var(--footer-ink);
  }
</style>
</head>
<body>
<main class="card">
  <svg class="card__waves" width="1200" height="675" viewBox="0 0 1200 675" aria-hidden="true">
    <path fill="var(--wave-1)" d="M0 0 L330 0 C 540 140 720 420 1200 500 L1200 675 L0 675 Z"/>
    <path fill="var(--wave-2)" d="M0 40 C 320 40 560 360 1200 545 L1200 675 L0 675 Z"/>
    <path fill="var(--wave-3)" d="M0 150 C 360 150 620 460 1200 590 L1200 675 L0 675 Z"/>
    <path fill="var(--wave-4)" d="M0 270 C 360 270 660 520 1200 630 L1200 675 L0 675 Z"/>
    <path fill="var(--wave-5)" d="M0 400 C 320 390 640 570 1200 675 L0 675 Z"/>
    <path fill="var(--wave-teal)" opacity="0.7" d="M0 590 C 420 560 820 640 1200 610 L1200 675 L0 675 Z"/>
  </svg>

  <header class="brand">
    <span class="brand__mark"></span>
    <h1 class="brand__name">KORVANT INC</h1>
    <span class="brand__rule"></span>
    <p class="brand__tagline">READY-SET-GO</p>
  </header>

  <section class="person">
    <h2 class="person__name">DANIEL MARLOW</h2>
    <p class="person__title">Lender CEO</p>
  </section>

  <dl class="contact">
    <dt>Phone:</dt><dd>555-014-2283</dd>
    <dt>E-Mail:</dt><dd>daniel@korvantinc.com</dd>
    <dt>Web:</dt><dd>www.korvantinc.com</dd>
  </dl>

  <p class="footer-note">Northfield Capital Group Inc.<br>Backed Financial Provider A.S.A.P Lender</p>
</main>
</body>
</html>
```